High profile consultancy

We need a web design for a company called VN Services. VN as abbreviation for Verdant North.

Company focusses on Sourcing (VN Sourcing, focus on ICT), Metrics (VN Metrics; focus on business case analysis and trends in ICT) and Software (VN software; to be developed later on; mainly tools supporting VN soucing and metrics)

Customers base consists of large enterprises, >1000 employees.

Site needs to have menu's for
- services
- login
- about
and a special area ' inspire ' to be able to communicate topics that should inspire our customers to contact us.

but key; it schould communicate our expertise and focus on deep knowlegde of ICT sourcing

Reason: please advice on content management systems to be used to maintain site also please advice on Plimzo search bidlines. Will provide feedback on designs shortly.

Target Market(s)

CIO's; board of directors;
company excels in ICT / business knowledge and ability to execute; creates / optimizes relations between ICT suppliers and enterprises.

Requirements
Must have
• website should be easily be found; adaptive by design; accessible by all browsers.
• Need to have a login section for later use
Nice to have
• usage of (draft) logo. see upload.

```html
<!DOCTYPE html>
<html lang="en">
<head>
<meta charset="utf-8">
<title>VN Services</title>
<link href="https://fonts.googleapis.com/css2?family=Oxygen:wght@400;700&family=Fenix&display=swap" rel="stylesheet">
<style>
:root{
  --blue:#0b63ad;
  --blue-dark:#0a4382;
  --text:#4a4a4a;
  --heading:#444;
  --nav:#3a3a3a;
  --rule:#c9c9c9;
  --card-bg:#f7f7f7;
  --card-border:#d6d6d6;
  --foot-top:#0aa3d8;
  --foot-bottom:#066aa6;
}
*{box-sizing:border-box;margin:0;padding:0}
html,body{width:1200px;height:1158px;overflow:hidden}
body{position:relative;font-family:"Oxygen",sans-serif;color:var(--text);
  background:linear-gradient(#e3e3e3 486px,#ffffff 720px,#f3f3f3 1054px)}
.abs{position:absolute}

/* header */
.site-header{position:absolute;left:0;top:0;width:1200px;height:107px;
  background:linear-gradient(#ffffff,#f1f1f1 60%,#e4e4e4);box-shadow:0 2px 4px rgba(0,0,0,.25);z-index:2}
.brand{position:absolute;left:133px;top:30px;display:flex;align-items:center;gap:12px;
  font-family:"Oxygen",sans-serif;font-weight:700;font-size:40px;color:var(--blue);letter-spacing:-0.5px}
.brand-dot{width:34px;height:34px;border-radius:50%;background:var(--blue)}
.phone{position:absolute;left:788px;top:12px;display:flex;align-items:center;gap:10px;
  font-size:19px;font-weight:700;color:#333}
.account{position:absolute;left:966px;top:15px;font-size:13px;color:#333}
.account span{margin:0 8px;color:#666}
.main-nav{position:absolute;top:61px;left:625px;height:35px;display:flex;align-items:center}
.main-nav a{text-decoration:none;color:var(--nav);font-size:15px;font-weight:700;letter-spacing:.3px}
.nav-active{display:flex;align-items:center;justify-content:center;width:113px;height:35px;border-radius:4px;
  background:linear-gradient(#1769b9,#0a3f80);color:#fff!important}
.nav-about{margin-left:33px}.nav-inspire{margin-left:39px}.nav-contact{margin-left:40px}

/* hero */
.hero{position:absolute;left:0;top:107px;width:1200px;height:379px;
  background:linear-gradient(100deg,#dfe4ea 0%,#8b8f95 22%,#e6e8ea 45%,#c9ccd0 65%,#3c4656 85%,#dadfe4 100%)}
.hero-caption{position:absolute;left:0;bottom:0;width:1200px;height:43px;background:rgba(70,80,100,.72)}
.hero-caption p{position:absolute;left:136px;top:3px;font-family:"Fenix",serif;font-size:29px;color:#fff}
.slider-dots{position:absolute;left:970px;bottom:0;width:94px;height:24px;background:#eaeaea;
  border-radius:16px 16px 0 0;display:flex;gap:6px;justify-content:center;align-items:center;padding-top:2px}
.slider-dots i{width:9px;height:9px;border-radius:50%;background:#8a9099}
.slider-dots i:first-child{background:#3e4f68}

/* welcome */
.welcome{position:absolute;left:136px;top:505px;width:680px}
.section-title{font-size:22px;font-weight:400;color:var(--heading);padding-left:58px;height:34px;
  border-bottom:1px dashed var(--rule)}
.welcome p{font-size:12.3px;line-height:18.3px;margin-top:9px}
.welcome p+p{margin-top:8px}
.more-link{display:block;text-align:right;color:var(--blue);font-size:12.5px;text-decoration:underline;margin-top:4px}

/* service cards */
.card{position:absolute;top:741px;width:216px;height:272px;background:var(--card-bg);
  border:1px solid var(--card-border);border-radius:4px;box-shadow:0 12px 12px -10px rgba(0,0,0,.15)}
.card h3{position:absolute;left:9px;top:10px;font-size:19.5px;font-weight:400;color:var(--blue)}
.card p{position:absolute;left:11px;top:44px;width:200px;font-size:12.3px;line-height:16.5px;color:#333}
.card .card-more{position:absolute;left:11px;top:100px;font-size:11.5px;font-weight:700;color:var(--blue);text-decoration:none}
.card-image{position:absolute;left:9px;top:127px;width:197px;height:113px;border-radius:4px;
  box-shadow:0 6px 8px rgba(0,0,0,.25)}

/* sidebar */
.sidebar{position:absolute;left:834px;top:518px;width:235px;height:495px;background:var(--card-bg);
  border:1px solid var(--card-border);border-radius:4px;padding:8px 10px 0 11px}
.sidebar h2{font-size:22px;font-weight:400;color:var(--heading);padding-left:58px;height:34px;border-bottom:1px solid var(--rule)}
.inspire-item{font-size:12.3px;line-height:18.3px;padding:6px 0 8px;border-bottom:1px solid #e2e2e2}
.inspire-item:last-of-type{border-bottom:0}
.inspire-item a{display:block;color:var(--blue);font-weight:700;text-decoration:none}
.view-all{position:absolute;right:9px;bottom:12px;font-size:12.5px;color:var(--blue);text-decoration:underline}

/* footer */
.site-footer{position:absolute;left:0;top:1054px;width:1200px;height:104px;
  background:linear-gradient(var(--foot-top),var(--foot-bottom))}
.footer-nav{position:absolute;left:134px;top:26px;display:flex;font-family:"Fenix",serif;font-size:15px}
.footer-nav a{color:#fff;text-decoration:none;padding:0 14px;border-left:1px solid rgba(255,255,255,.7)}
.footer-nav a:first-child{padding-left:0;border-left:0}
.copyright{position:absolute;left:134px;top:60px;color:#fff;font-size:12.5px}
.subscribe-title{position:absolute;left:548px;top:24px;font-family:"Fenix",serif;font-size:16px;color:#fff}
.subscribe-input{position:absolute;left:547px;top:53px;width:212px;height:23px;background:#fff;border:1px solid #bbb;
  font-size:11px;font-style:italic;color:#999;padding:4px 7px}
.subscribe-btn{position:absolute;left:759px;top:53px;width:54px;height:23px;background:#222;color:#fff;font-size:13px;
  display:flex;align-items:center;justify-content:center}
.footer-brand{position:absolute;left:935px;top:38px;font-weight:700;font-size:27px;color:#0a3f80}
</style>
</head>
<body>

<header class="site-header">
  <div class="brand"><span class="brand-dot"></span>VN Services</div>
  <div class="phone">
    <svg width="28" height="24" viewBox="0 0 28 24"><path d="M2 9c0-6 24-6 24 0v2h-6V8c-3-1-9-1-12 0v3H2z" fill="#0b63ad"/><g fill="#0b63ad"><circle cx="9" cy="15" r="1.8"/><circle cx="14" cy="15" r="1.8"/><circle cx="19" cy="15" r="1.8"/><circle cx="9" cy="20" r="1.8"/><circle cx="14" cy="20" r="1.8"/><circle cx="19" cy="20" r="1.8"/></g></svg>
    555-014-2290
  </div>
  <div class="account">Login<span>|</span>Register</div>
  <nav class="main-nav">
    <a class="nav-active" href="#">SERVICES</a>
    <a class="nav-about" href="#">ABOUT US</a>
    <a class="nav-inspire" href="#">INSPIRE</a>
    <a class="nav-contact" href="#">CONTACT US</a>
  </nav>
</header>

<section class="hero" role="img" aria-label="Photo of three business people smiling in a meeting">
  <div class="hero-caption"><p>Lorem ipsum dolor sit amet, consectetuer adipiscing elit.</p></div>
  <div class="slider-dots"><i></i><i></i><i></i><i></i></div>
</section>

<section class="welcome">
  <h1 class="section-title">Welcome to VN Services</h1>
  <p>Lorem ipsum dolor sit amet, consectetuer adipiscing elit, sed diam nonummy nibh euismod tincidunt ut sit laoreet amet dolore magna aliquam erat volutpat. Ut wisi enim ad minim veniam, quis nostrud exerci tation ame ullamcorper suscipit lobortis nisl ut aliquip ex ea commodo consequat. Duis autem vel eum iriure dolor in hendrerit in vulputate velit essetr molestie consequat, vel illum dolore eu feugiat nulla facilisis at vero eros et accumsan et iusto odio dignissim quiamet blandit praesent luptatum zzril delenit augue duis dolore te feugait nulla facilisi.vel illum dolore eu feugiat nulla amet facilisis at vero eros et accumsan et iusto odio dignissim.</p>
  <p>Duis autem vel eum iriure dolor in hendrerit in vulputate velit essetr molestie consequat, vel illum dolore eu feugiat amet nulla facilisis at vero eros et accumsan et iusto odio dignissim quiamet blandit praesent luptatum...</p>
  <a class="more-link" href="#">READ MORE</a>
</section>

<article class="card" style="left:131px">
  <h3>VN ICT SOURCING</h3>
  <p>Lorem ipsum dolor sit amet herem ctetuer adipiscing elit, sed diam ummy nibh euismod tincidunt sit</p>
  <a class="card-more" href="#">Read More &rarr;</a>
  <div class="card-image" role="img" aria-label="Photo of a cheering office team" style="background:linear-gradient(#e9edf2,#9aa6b4)"></div>
</article>
<article class="card" style="left:366px">
  <h3>VN METRICS</h3>
  <p>Lorem ipsum dolor sit amet here ctetuer adipiscing elit, sed diam ummy nibh euismod tincidunt</p>
  <a class="card-more" href="#">Read More &rarr;</a>
  <div class="card-image" role="img" aria-label="Illustration of business figures with charts and a world map" style="background:linear-gradient(#9aa3ad,#3d444d)"></div>
</article>
<article class="card" style="left:600px">
  <h3>VN SOFTWARE</h3>
  <p>Lorem ipsum dolor sit amet sit ctetuer adipiscing elit, sed diamat ummy nibh euismod tincidunt</p>
  <a class="card-more" href="#">Read More &rarr;</a>
  <div class="card-image" role="img" aria-label="Photo of a hand holding a tablet with a glowing globe" style="background:linear-gradient(#5a7a9a,#1d2a3a)"></div>
</article>

<aside class="sidebar">
  <h2>Inspire</h2>
  <div class="inspire-item">Lorem ipsum dolor sit amet adipiseing elit, sed diam nonummy nibh euismod tincidunt ut sit laoreet dolore magna aliqum erat voltpat. Ut wisi enim set minim veniam, quis nostrud suscipit lobortis nisl ut aliquip ex ea comodo consequat nummy amet sit.<a href="#">Lorem Ipsum</a></div>
  <div class="inspire-item">Ut wisi enim set minim veniam, quis nostrud suscipit lobortis nisl ut amet aliquip ex ea comodo consequat sit nummy amet sit.<a href="#">Lorem Ipsum</a></div>
  <div class="inspire-item">Lorem ipsum dolor sit amet adipiseing elit, sed diam nonummy nibh euismod tincidunt ut sit laoreet dolore magna aliqum erat voltpat. Ut wisi enim setr minim veniam, quis nostrud suscipitt lobortis nisl ut aliquip ex ea comodo consequat nummy amet sit.<a href="#">Lorem Ipsum</a></div>
  <a class="view-all" href="#">VIEW ALL</a>
</aside>

<footer class="site-footer">
  <nav class="footer-nav">
    <a href="#">Services</a><a href="#">About Us</a><a href="#">Inspire</a><a href="#">Contact Us</a>
  </nav>
  <div class="copyright">Copyright &copy; 2013 VN Services.&nbsp; All Rights Reserved.</div>
  <div class="subscribe-title">Subscribe to Newsletter</div>
  <div class="subscribe-input">enter you email address here..</div>
  <div class="subscribe-btn">Submit</div>
  <div class="footer-brand">VN Services</div>
</footer>

</body>
</html>
```